Veteran Owned General Contractor needs Bold New Business Cards

We are a service disabled veteran owned small business. We're a general contractor that specializes in excavation, underground utilities, site work, land clearing and demolition. We would like a fresh, simple, bold, new look for our business cards. We're open to ideas! We'd like to incorporate the following information on the card:

Company Name & Logo, Name of Person, Job Title, Office Phone, Fax, Cell Phone, Email Address, Website, SDVOSB

Our logo is included. We look forward to your thoughts.

Thank you!
Updates

Reason: Hello Due to the overwhelming response to this project, we are extending the deadline one time to allow for improved communication and feedback with the top candidates. We would like to thank everyone for their hard work and exceptional creativity! Thank you

Industry/Entity Type

Business

Contact Information for Business Card

Font styles to use
Sans Serif

Requirements
Nice to have
• As we are a veteran owned company, it would be nice to incorporate an American flag into the design. Maybe on the back?

```html
<!DOCTYPE html>
<html lang="en">
<head>
<meta charset="utf-8">
<title>Ironside Inc — Business Card</title>
<link rel="stylesheet" href="https://fonts.googleapis.com/css2?family=Arimo:ital,wght@0,400;0,700;1,700&display=swap">
<style>
  :root {
    --backdrop: #aba9a5;
    --label: #3b3f6b;
    --card: #1e1e1e;
    --stripe: #e4e4e4;
    --brand-green: #8cc63f;
    --text-light: #ffffff;
    --flag-blue: #4a5a8c;
    --flag-light: #d9d4d6;
    --flag-red: #b8434f;
  }
  * { margin: 0; padding: 0; box-sizing: border-box; }
  html, body { width: 800px; height: 1200px; overflow: hidden; }
  body {
    background: var(--backdrop);
    font-family: "Arimo", Arial, sans-serif;
    position: relative;
  }
  .side-label {
    position: absolute;
    left: 0; width: 800px;
    text-align: center;
    color: var(--label);
    font-weight: 700;
    font-size: 32px;
    letter-spacing: 1px;
  }
  .side-label--front { top: 92px; }
  .side-label--back { top: 628px; }

  .card {
    position: absolute;
    left: 48px; width: 704px;
    background: var(--card);
    overflow: hidden;
  }
  .card--front { top: 147px; height: 400px; }
  .card--back { top: 680px; height: 405px; }

  .hazard-band {
    position: absolute;
    left: 0; right: 0;
    height: 26px;
    background: repeating-linear-gradient(-60deg, var(--stripe) 0 34px, transparent 34px 78px);
  }
  .hazard-band--top { top: 6px; }
  .hazard-band--bottom { bottom: 6px; }

  .brand-mark {
    position: absolute;
    left: 300px; top: 74px;
    width: 98px; height: 98px;
    background: var(--brand-green);
    border-radius: 8px;
  }
  .brand-name {
    position: absolute;
    left: 0; right: 0; top: 226px;
    text-align: center;
    color: var(--brand-green);
    font-weight: 700;
    font-size: 72px;
    letter-spacing: 4px;
  }

  .flag-area {
    position: absolute;
    left: 59px; top: 72px;
    width: 308px; height: 187px;
    background: linear-gradient(120deg, var(--flag-blue) 0%, var(--flag-light) 50%, var(--flag-red) 100%);
  }
  .contact {
    position: absolute;
    left: 421px; top: 78px;
    color: var(--text-light);
  }
  .contact__name { font-weight: 700; font-size: 31px; line-height: 36px; }
  .contact__title { font-weight: 700; font-style: italic; font-size: 21px; line-height: 28px; }
  .contact__lines { margin-top: 16px; font-size: 23px; line-height: 29.5px; }
  .contact__lines + .contact__lines { margin-top: 16px; }

  .brand-small {
    position: absolute;
    left: 59px; top: 304px;
    display: flex; align-items: center; gap: 10px;
  }
  .brand-small__mark {
    width: 34px; height: 34px;
    background: var(--brand-green);
    border-radius: 4px;
  }
  .brand-small__name {
    color: var(--brand-green);
    font-weight: 700;
    font-size: 30px;
    letter-spacing: 1px;
  }
</style>
</head>
<body>
  <div class="side-label side-label--front">FRONT</div>
  <section class="card card--front">
    <div class="hazard-band hazard-band--top"></div>
    <div class="brand-mark"></div>
    <div class="brand-name">IRONSIDE INC</div>
    <div class="hazard-band hazard-band--bottom"></div>
  </section>

  <div class="side-label side-label--back">BACK</div>
  <section class="card card--back">
    <div class="hazard-band hazard-band--top"></div>
    <div class="flag-area" role="img" aria-label="Photo of a waving American flag"></div>
    <div class="contact">
      <div class="contact__name">Your Name</div>
      <div class="contact__title">Owner</div>
      <div class="contact__lines">
        <div>Office: 123 456 789</div>
        <div>Fax: 123 456 789</div>
        <div>Cell: 123 456 789</div>
      </div>
      <div class="contact__lines">
        <div>Email: 12345@abc</div>
        <div>Website: abcd.com</div>
        <div>SDVOSB:</div>
      </div>
    </div>
    <div class="brand-small">
      <div class="brand-small__mark"></div>
      <div class="brand-small__name">IRONSIDE INC</div>
    </div>
    <div class="hazard-band hazard-band--bottom"></div>
  </section>
</body>
</html>
```